Kestrel Works Wall Art Design

Our local government has developed a department called the "Kestrel Works" which has been running for a few years. Our purpose is to encourage staff to think Under the Willow and engage their problems in new ways. We offer tools and services which enable collaboration between people and other departments, one such tool is our new meeting room. We've designed this space with the intention of encouraging creativity and allowing staff members to break away from the ordinary working environment. Attached are photos of the room.
The room is called "Under the Willow". In one photo you will see our Under the Willow sign filling the space where'd we'd like to have the design on, however we would like to stay away from naming labels in our design to convey to staff that this is their space as well, rather than the Kestrel Works' special little room. We would like a design that embodies the spirit of our department. We've talked about what that means to us and we've stepped it out as;
Investigate
Collaborate
Innovate
Create
Celebrate
We had ideas of having a funky word jumble design or something creative to use these words, but we'd love to see anything else that conveys a feeling of creativity.
The size of the art is limited to 1400mm x 2800mm

```html
<!DOCTYPE html>
<html lang="en">
<head>
<meta charset="utf-8">
<title>Kestrel Works Wall Art – Word Jumble</title>
<link rel="stylesheet" href="https://fonts.googleapis.com/css2?family=Noto+Sans+Mono:wght@400;700&family=Indie+Flower&family=Courier+Prime:wght@700&display=swap">
<style>
  :root {
    --frame: #a9a9a9;
    --paper-light: #ffffff;
    --paper-edge: #ececec;
    --orange: #ff6a00;
    --orange-soft: #f5841f;
    --blue: #08a8e8;
    --grey-text: #707070;
    --grey-faint: #c4c4c4;
    --arrow: #9a9a9a;
  }
  html, body {
    margin: 0;
    width: 1200px;
    height: 1200px;
    overflow: hidden;
    background: var(--frame);
  }
  .wall-art { display: block; width: 1200px; height: 1200px; }
  .mono-bold { font-family: "Noto Sans Mono", monospace; font-weight: 700; }
  .mono { font-family: "Noto Sans Mono", monospace; font-weight: 400; }
  .hand { font-family: "Indie Flower", cursive; }
  .key-word { fill: var(--orange); font-size: 44px; }
  .key-word-hand { fill: var(--orange-soft); font-size: 50px; }
  .link-word { fill: var(--blue); font-size: 22px; }
  .link-word-grey { fill: var(--grey-text); font-size: 25px; }
  .motto-line {
    font-family: "Courier Prime", monospace;
    font-weight: 700;
    font-size: 11.5px;
    fill: var(--grey-faint);
  }
  .arrow { fill: var(--arrow); }
  text { dominant-baseline: central; text-anchor: middle; }
  .align-end { text-anchor: end; }
  .align-start { text-anchor: start; }
</style>
</head>
<body>
<svg class="wall-art" viewBox="0 0 1500 1500" xmlns="http://www.w3.org/2000/svg">
  <defs>
    <radialGradient id="paper" cx="0.5" cy="0.55" r="0.75">
      <stop offset="0" stop-color="var(--paper-light)"/>
      <stop offset="1" stop-color="var(--paper-edge)"/>
    </radialGradient>
    <pattern id="dot-grid" width="8" height="8" patternUnits="userSpaceOnUse">
      <circle cx="4" cy="4" r="1.2" fill="#c8c8c8"/>
    </pattern>
    <linearGradient id="fade-left" x1="0" y1="0" x2="1" y2="1">
      <stop offset="0" stop-color="#000"/>
      <stop offset="1" stop-color="#fff"/>
    </linearGradient>
    <linearGradient id="fade-down" x1="1" y1="0" x2="0" y2="1">
      <stop offset="0" stop-color="#000"/>
      <stop offset="0.4" stop-color="#fff"/>
      <stop offset="1" stop-color="#000"/>
    </linearGradient>
    <mask id="mask-left"><rect x="148" y="295" width="158" height="90" fill="url(#fade-left)"/></mask>
    <mask id="mask-right"><rect x="1336" y="110" width="134" height="62" fill="url(#fade-down)"/></mask>

    <g id="motto-block">
      <text class="motto-line align-end" x="1468" y="85">INVESTIGATE COLLABORATE INNOVATE CREATE CELEBRATE</text>
      <text class="motto-line align-end" x="1468" y="99">INVESTIGATE COLLABORATE INNOVATE CREATE CELEBRATE</text>
      <rect x="1336" y="110" width="134" height="62" fill="url(#dot-grid)" mask="url(#mask-right)"/>
      <rect x="148" y="295" width="158" height="90" fill="url(#dot-grid)" mask="url(#mask-left)"/>
      <text class="motto-line align-start" transform="translate(317,295) rotate(90)" x="0" y="0">INVESTIGATE COLLABORATE INNOVATE CREATE CELEBRATE</text>
      <text class="motto-line align-start" transform="translate(336,295) rotate(90)" x="0" y="0">INVESTIGATE COLLABORATE INNOVATE CREATE CELEBRATE</text>
    </g>
  </defs>

  <!-- Version one: bold mono, orange and blue -->
  <g class="panel panel-mono">
    <rect x="22" y="10" width="1456" height="728" fill="url(#paper)"/>
    <use href="#motto-block"/>

    <text class="mono-bold key-word" x="137 186 235 284 333 382 431 480 529 578 627" y="162">Investigate</text>
    <text class="mono-bold key-word" x="578 627 676 725 774 823 872 921 1019 1068" y="287">Collaborrte</text>
    <text class="mono-bold key-word" x="578 627 676 725 774 823 872 921" y="287" style="opacity:0">.</text>
    <text class="mono-bold key-word" transform="translate(975,43) rotate(90)" x="0 49 97 146 195 293" y="0">Innovt</text>
    <circle cx="970" cy="289" r="22" fill="none" stroke="var(--blue)" stroke-width="2.5"/>
    <text class="mono-bold" x="970" y="289" fill="var(--blue)" font-size="30" transform="rotate(90 970 289)">a</text>
    <text class="mono-bold key-word" x="722 771 820 869 918 967" y="385">Create</text>
    <text class="mono-bold key-word" x="968 1017 1066 1115 1164 1214 1263 1312 1362" y="515">Celebrate</text>

    <text class="mono-bold link-word" x="333 333 333 333" y="73 99 125 203">firt</text>
    <text class="mono-bold link-word" x="628 628 628" y="75 101 127">tak</text>
    <text class="mono-bold link-word" x="627 627 627" y="248 325 350">yur</text>
    <text class="mono-bold link-word" x="627 627 627 627" y="428 455 481 508">time</text>
    <text class="mono-bold link-word align-end" x="944" y="110">Don’t be</text>
    <text class="mono-bold link-word align-end" x="944" y="141">afraid</text>
    <text class="mono-bold link-word" x="940" y="191">t</text>
    <text class="mono-bold link-word" x="1009 1036 1063" y="340">ime</text>
    <text class="mono-bold link-word" transform="translate(1060,387) rotate(90)" x="0" y="0">To</text>
    <text class="mono-bold link-word" x="771 771 771 771" y="345 424 450 476">Geat</text>
    <text class="mono-bold link-word" x="690 717 745 799" y="450">Ides</text>
    <text class="mono-bold link-word" x="1215 1215 1215" y="429 455 481">you</text>
    <text class="mono-bold link-word align-end" x="1370" y="551">success</text>

    <path class="arrow" d="M1043 432 L1060 446 L1077 432 L1060 467 Z"/>
  </g>

  <!-- Version two: hand-set orange with grey links -->
  <g class="panel panel-hand">
    <rect x="22" y="758" width="1460" height="729" fill="url(#paper)"/>
    <use href="#motto-block" transform="translate(3,748)"/>

    <text class="hand key-word-hand" x="105 150 195 240 285 330 375 420 465 510 557" y="928">Investigate</text>
    <text class="hand key-word-hand" x="507 555 600 636 676 723 772 818 912 958" y="1072">Collaborte</text>
    <text class="hand key-word-hand" transform="translate(865,830) rotate(90)" x="0 47 95 142 192 288" y="0">Innovt</text>
    <circle cx="863" cy="1072" r="25" fill="none" stroke="var(--orange-soft)" stroke-width="2"/>
    <text class="mono" x="863" y="1072" fill="var(--grey-text)" font-size="30" transform="rotate(90 863 1072)">a</text>
    <text class="hand key-word-hand" x="627 673 718 765 812 860" y="1165">Create</text>
    <text class="hand key-word-hand" x="960 1006 1052 1098 1144 1190 1236 1282 1328" y="1297">Celebrate</text>

    <text class="mono link-word-grey" x="330 330 330 330" y="820 851 881 972">firt</text>
    <text class="mono link-word-grey" x="558 558 558" y="831 861 892">tak</text>
    <text class="mono link-word-grey" x="555 555 555" y="1027 1117 1147">yur</text>
    <text class="mono link-word-grey" x="555 555 555 555" y="1238 1268 1299 1329">time</text>
    <text class="mono link-word-grey align-end" x="833" y="880">Don’t be</text>
    <text class="mono link-word-grey align-end" x="833" y="916">afraid</text>
    <text class="mono link-word-grey" x="828" y="971">t</text>
    <text class="mono link-word-grey" x="900 932 965" y="1120">ime</text>
    <text class="mono link-word-grey" transform="translate(965,1175) rotate(90)" x="0" y="0">To</text>
    <text class="mono link-word-grey" x="718 718 718" y="1137 1199 1229">Gea</text>
    <text class="mono link-word-grey" x="623 654 686 718 750" y="1259">Idets</text>
    <text class="mono link-word-grey" x="1187 1187 1187" y="1205 1235 1265">you</text>
    <text class="mono link-word-grey align-end" x="1424" y="1339" letter-spacing="2">success</text>

    <path class="arrow" d="M947 1218 L964 1232 L981 1218 L964 1253 Z"/>
  </g>
</svg>
</body>
</html>
```